New Business Card Design Project

Looking for a modern business card design for an import distribution business for industrial technical products. The winning design will translate modern, sophistication, technical, professional and sustainable.

Target Market(s)

Technical customers

Industry/Entity Type

Business

Contact Information for Business Card

Dean Harlow
Sales Manager
M: 0471 625 183
P: 1300 872 619
dean@volkarsystems.com.au
4/18 Galloway Crest Road
Brackenvale NSW 2158
www.volkarsystems.com.au

Font styles to use
Sans Serif

Colors
ec1f27
606060
000000
fbfbfb

Requirements
Must have
• My Logo which is the Volkar Systems logo attached
Nice to have
• Eurostile Bold font

```html
<!DOCTYPE html>
<html lang="en">
<head>
<meta charset="utf-8">
<title>Volkar Systems – Business Card</title>
<link rel="stylesheet" href="https://fonts.googleapis.com/css2?family=Roboto:wght@400;500;700&display=swap">
<style>
  :root {
    --red: #ec1f27;
    --red-deep: #d42a25;
    --grey: #606060;
    --grey-block: #6b7079;
    --ink: #000000;
    --paper: #fbfbfb;
    --backdrop: #e9e6e1;
    --band-light: #e6e6e6;
  }
  * { margin: 0; padding: 0; box-sizing: border-box; }
  html, body { width: 1200px; height: 1023px; overflow: hidden; }
  body {
    background: var(--backdrop);
    font-family: "Roboto", Arial, sans-serif;
    position: relative;
  }
  .card {
    position: absolute;
    width: 600px;
    height: 343px;
    left: 300px;
    overflow: hidden;
    box-shadow: 0 6px 18px rgba(0,0,0,.18);
  }
  /* Front */
  .card--front { top: 90px; background: var(--paper); }
  .brand {
    position: absolute;
    left: 44px;
    top: 62px;
    display: flex;
    align-items: center;
    gap: 14px;
  }
  .brand__square { width: 40px; height: 40px; background: var(--red); flex: none; }
  .brand__name {
    font-weight: 700;
    font-size: 40px;
    letter-spacing: 1px;
    text-transform: uppercase;
    color: var(--red);
    white-space: nowrap;
  }
  .accent-block {
    position: absolute;
    left: 486px; top: 88px;
    width: 78px; height: 52px;
    background: var(--grey-block);
  }
  .name-band {
    position: absolute;
    left: 0; top: 148px;
    width: 470px; height: 56px;
    background: var(--red);
    color: var(--paper);
    padding: 9px 0 0 56px;
  }
  .name-band__name { font-size: 19px; font-weight: 500; line-height: 1.1; }
  .name-band__title { font-size: 13px; line-height: 1.3; }
  .contacts {
    position: absolute;
    left: 56px; top: 224px;
    list-style: none;
    color: var(--grey);
    font-size: 15px;
  }
  .contacts li { display: flex; align-items: center; gap: 9px; line-height: 22px; white-space: nowrap; }
  .contacts svg { width: 13px; height: 13px; flex: none; }
  .address {
    position: absolute;
    right: 36px; top: 224px;
    text-align: right;
    color: var(--grey);
    font-size: 14px;
    line-height: 20px;
    font-style: normal;
    white-space: nowrap;
  }
  .edge-line {
    position: absolute;
    left: 0; right: 0; bottom: 14px;
    height: 3px;
    background: var(--grey-block);
  }
  .edge-strip {
    position: absolute;
    left: 0; right: 0; bottom: 0;
    height: 10px;
    background: var(--red);
  }
  /* Back */
  .card--back { top: 553px; background: var(--red-deep); }
  .card--back .brand {
    left: 0; right: 0; top: 118px;
    justify-content: center;
  }
  .card--back .brand__square { background: var(--paper); }
  .card--back .brand__name { color: var(--paper); }
  .web-band {
    position: absolute;
    left: 0; right: 0; bottom: 34px;
    height: 40px;
    background: var(--band-light);
    display: flex;
    align-items: center;
    justify-content: center;
    color: var(--grey);
    font-size: 13px;
    letter-spacing: 4px;
  }
</style>
</head>
<body>

<section class="card card--front" aria-label="Business card front">
  <div class="brand">
    <span class="brand__square"></span>
    <span class="brand__name">Volkar Systems</span>
  </div>
  <div class="accent-block"></div>
  <div class="name-band">
    <p class="name-band__name">Dean Harlow</p>
    <p class="name-band__title">Sales Manager</p>
  </div>
  <ul class="contacts">
    <li>
      <svg viewBox="0 0 14 14"><rect x="1" y="1" width="12" height="12" rx="2" fill="#ec1f27"/><rect x="4" y="4" width="6" height="3" fill="#fbfbfb"/><rect x="4" y="8" width="6" height="2" fill="#fbfbfb"/></svg>
      1300 872 619
    </li>
    <li>
      <svg viewBox="0 0 14 14"><rect x="3" y="0.5" width="8" height="13" rx="1.5" fill="#ec1f27"/><rect x="4.5" y="2.5" width="5" height="7" fill="#fbfbfb"/></svg>
      0471 625 183
    </li>
    <li>
      <svg viewBox="0 0 14 14"><rect x="0.5" y="2.5" width="13" height="9" fill="#ec1f27"/><path d="M1 3 L7 8 L13 3" stroke="#fbfbfb" stroke-width="1.3" fill="none"/></svg>
      dean@volkarsystems.com.au
    </li>
    <li>
      <svg viewBox="0 0 14 14"><circle cx="7" cy="7" r="6" fill="none" stroke="#ec1f27" stroke-width="1.4"/><ellipse cx="7" cy="7" rx="2.6" ry="6" fill="none" stroke="#ec1f27" stroke-width="1.1"/><path d="M1 7 H13" stroke="#ec1f27" stroke-width="1.1"/></svg>
      www.volkarsystems.com.au
    </li>
  </ul>
  <address class="address">
    4/18 Galloway Crest Road<br>
    Brackenvale NSW 2158
  </address>
  <div class="edge-line"></div>
  <div class="edge-strip"></div>
</section>

<section class="card card--back" aria-label="Business card back">
  <div class="brand">
    <span class="brand__square"></span>
    <span class="brand__name">Volkar Systems</span>
  </div>
  <div class="web-band">www.volkarsystems.com.au</div>
</section>

</body>
</html>
```